Signage. Will be for store front. Building is on a corner lot. Lots of traffic.

Opening a new location for our landscape business with a garden store (boutique theme) which will have big pottery pots, house plants, ferns and orchids for sale.

And on the side lot of the store we will have bigger bulk items(contractors theme) landscape plants, sod, mulch, soil, rock for sale.

Sign is about 8’x6’

Target Market(s)

Home owners
Landscapers
Builders

Industry/Entity Type

Landscaping

Font styles to use
Sans Serif

Colors
9bcb3c

Requirements
Must have
• “ Installation and Delivery” is a big deal to let people know we do that
Nice to have
• Added a first rendition idea but don’t love it
Added a file with some words to play with
Need help with the words
Should not have
• ?

```html
<!DOCTYPE html>
<html lang="en">
<head>
<meta charset="utf-8">
<title>Fernway Gardens – Storefront Sign</title>
<link href="https://fonts.googleapis.com/css2?family=Montserrat:wght@600;700;800&family=Cookie&display=swap" rel="stylesheet">
<style>
  :root {
    --page-bg: #e8edf1;
    --sign-white: #ffffff;
    --band-grey: #e0e2e1;
    --ink: #0b0b0b;
    --leaf-green: #74963f;
    --forest-green: #55682d;
    --script-green: #5b7330;
  }
  html, body {
    margin: 0;
    padding: 0;
    width: 1200px;
    height: 900px;
    overflow: hidden;
    background: var(--page-bg);
    font-family: "Montserrat", Arial, sans-serif;
  }
  .sign {
    position: absolute;
    left: 40px;
    top: 90px;
    width: 1120px;
    height: 720px;
    background: var(--sign-white);
    box-shadow: 0 6px 24px rgba(0,0,0,0.12);
  }
  .brand-band {
    height: 172px;
    display: flex;
    align-items: center;
    justify-content: center;
    gap: 18px;
  }
  .brand-dot {
    width: 30px;
    height: 30px;
    border-radius: 50%;
    background: var(--leaf-green);
  }
  .brand-name {
    font-weight: 700;
    font-size: 52px;
    letter-spacing: 6px;
    text-transform: uppercase;
    color: var(--leaf-green);
  }
  .services-band {
    height: 213px;
    background: var(--band-grey);
    display: flex;
    flex-direction: column;
    justify-content: center;
    align-items: center;
    gap: 0;
  }
  .services-line {
    font-weight: 700;
    font-size: 66px;
    line-height: 76px;
    color: var(--ink);
    letter-spacing: -1px;
    display: flex;
    align-items: center;
    gap: 18px;
  }
  .divider {
    display: inline-block;
    width: 5px;
    height: 58px;
    background: var(--ink);
  }
  .welcome {
    font-family: "Cookie", "Brush Script MT", cursive;
    font-size: 86px;
    line-height: 1;
    color: var(--script-green);
    text-align: center;
    margin-top: 16px;
    height: 92px;
  }
  .phone-bar {
    position: absolute;
    left: 67px;
    top: 492px;
    width: 983px;
    height: 126px;
    background: var(--forest-green);
    display: flex;
    align-items: center;
    justify-content: center;
    gap: 20px;
    color: var(--sign-white);
  }
  .phone-icon { width: 86px; height: 86px; }
  .phone-number {
    font-weight: 700;
    font-size: 84px;
    letter-spacing: -1px;
  }
  .service-promise {
    position: absolute;
    left: 0;
    right: 0;
    top: 640px;
    text-align: center;
    font-weight: 800;
    font-size: 46px;
    letter-spacing: -0.5px;
    color: var(--forest-green);
    text-transform: uppercase;
  }
</style>
</head>
<body>
  <main class="sign">
    <header class="brand-band">
      <span class="brand-name">Fernway</span>
      <span class="brand-dot"></span>
      <span class="brand-name">Gardens</span>
    </header>

    <section class="services-band">
      <div class="services-line">SOD <span class="divider"></span> LANDSCAPE SUPPLY</div>
      <div class="services-line">LAWN <span class="divider"></span> GARDEN <span class="divider"></span> NURSERY</div>
    </section>

    <p class="welcome" style="margin-bottom:0">Public Welcome!</p>

    <div class="phone-bar">
      <svg class="phone-icon" viewBox="0 0 100 100" aria-hidden="true">
        <path fill="#ffffff" d="M24 14c4-3 9-2 11 2l9 16c2 4 1 8-2 10l-6 4c3 9 11 19 20 24l5-5c3-3 7-3 10-1l15 10c4 3 5 8 2 12l-6 7c-5 5-13 6-20 3C40 85 18 62 11 42c-3-8-1-16 5-21z"/>
        <path fill="none" stroke="#ffffff" stroke-width="7" stroke-linecap="round" d="M55 30a16 16 0 0 1 15 15"/>
        <path fill="none" stroke="#ffffff" stroke-width="7" stroke-linecap="round" d="M57 14a32 32 0 0 1 29 29"/>
      </svg>
      <span class="phone-number">(555)014-2290</span>
    </div>

    <p class="service-promise" style="margin:0">Installation &amp; Delivery Available</p>
  </main>
</body>
</html>
```